Industrial services company requires brochure for new product

We are an industrial services company called Tern Valley Holdings. Our clients include major mining, oil and gas and infrastructure clients in Western Australia.

We require a 4 page brochure to feature a new paint removal machine we are bringing to the market in Western Australia.The document will be used predominantly electronically but should be of a quality that can be printed also.

The new machine is an innovative way of removing paint from steel structures as it does not use abrasive blasting to remove the paint. Instead it uses induction heating.

There are some major environmental and safety benefits to using this machine over traditional methods as there are no airborne particles, no noise and minimal waste. The environmental and safety benefits of the are the competitive advantage of the machine and should come through in the marketing.

I have provided as an attachment the proposed copy, the pics available for use, and the Tern Valley logo.

In general I am thinking page 1 (cover - hero pic/company logo), page 2 (machine information), page 3 (case study) page 4 (about us/contact details/logo etc) but am happy to look at other options.

The images I have attached are the highest quality I will have available.

Target Market(s)

Mining, oil and gas, government infrastructure clients. These are businesses

Industry/Entity Type

Oil And Gas

Requirements
Must have
• The majority of the text supplied as necessary to understand the technology.

```html
<!DOCTYPE html>
<html lang="en">
<head>
<meta charset="utf-8">
<title>Tern Valley Holdings – Brochure Page Three Options</title>
<link href="https://fonts.googleapis.com/css2?family=Didact+Gothic&family=Poppins:wght@300;400;600&display=swap" rel="stylesheet">
<style>
  :root {
    --board: #b9bcc0;
    --paper: #ffffff;
    --ink: #232323;
    --body-ink: #4a4a4a;
    --blue-light: #4db3e6;
    --blue-deep: #0f9bd8;
    --silhouette: #ececec;
    --band-black: #0c0c0c;
    --band-charcoal: #3a3a3a;
    --band-blue: #0f9bd8;
    --photo-dark: #2b303a;
    --photo-rust: #7a5a44;
    --photo-water: #4f6a55;
  }
  * { box-sizing: border-box; margin: 0; padding: 0; }
  html, body { width: 1200px; height: 1000px; overflow: hidden; }
  body { background: var(--board); position: relative; font-family: "Didact Gothic", sans-serif; }

  .board-label {
    position: absolute; left: 499px; top: 122px; width: 250px; height: 25px;
    background: #000; color: #fff; font-family: "Poppins", sans-serif; font-weight: 400;
    font-size: 15px; letter-spacing: 9px; text-align: center; line-height: 25px; padding-left: 9px;
  }
  .option-number {
    position: absolute; top: 198px; font-family: "Poppins", sans-serif; font-weight: 600;
    font-size: 17px; color: var(--ink);
  }

  .page {
    position: absolute; top: 247px; width: 360px; height: 516px;
    background: var(--paper); overflow: hidden;
    box-shadow: 0 3px 8px rgba(0,0,0,.35);
  }
  .page--one { left: 53px; }
  .page--two { left: 420px; }
  .page--three { left: 789px; }

  .site-silhouette { position: absolute; background: var(--silhouette); }

  .title { position: absolute; font-family: "Poppins", sans-serif; line-height: 1; white-space: nowrap; }
  .title .case { font-weight: 400; color: var(--blue-light); }
  .title .study { font-weight: 600; color: var(--ink); }

  .body-copy { position: absolute; font-size: 7.6px; line-height: 9.6px; color: var(--body-ink); }
  .body-copy p + p { margin-top: 9px; }

  .footer-band {
    position: absolute; left: 0; bottom: 0; width: 100%; height: 26px;
    color: #fff; font-size: 7.5px; font-style: italic; letter-spacing: 3.4px;
    text-align: center; line-height: 26px;
  }
  .page--one .footer-band { background: var(--band-black); }
  .page--two .footer-band { background: var(--band-charcoal); }
  .page--three .footer-band { background: var(--band-blue); }

  .art { position: absolute; left: 0; top: 0; }

  .photo {
    position: absolute;
    background: linear-gradient(160deg, var(--photo-dark) 0%, var(--photo-rust) 55%, var(--photo-water) 100%);
  }
</style>
</head>
<body>

<div class="board-label">PAGE THREE</div>
<div class="option-number" style="left:229px">1</div>
<div class="option-number" style="left:594px">2</div>
<div class="option-number" style="left:963px">3</div>

<!-- Option 1 -->
<section class="page page--one">
  <div class="site-silhouette" role="img" aria-label="Grey silhouette of cranes and scaffolding" style="left:250px;top:0;width:110px;height:165px;"></div>
  <div class="site-silhouette" role="img" aria-label="Grey silhouette of cranes, scaffolding and workers" style="left:0;top:265px;width:200px;height:225px;"></div>
  <h1 class="title" style="left:18px;top:33px;">
    <span class="case" style="font-size:21px;">CASE</span><span class="study" style="font-size:30px;">STUDY</span>
  </h1>
  <div class="body-copy" style="left:19px;top:72px;width:258px;">
    <p>Coral Bight Ports Authority planned extensive remediation works in the basement of a post marina berth in Saltmarsh Point. Early research discovered the presence of tar epoxy structural steel. A suitable method for removing the epoxy coal tar not compromise the health of operators and minimize contaminated waste was sought.<br>The Thermaclear induction was tested by Tern Valley Holdings and proven to be the safest and most environmentally friendly for disposal of the epoxy coal tar option.</p>
    <p style="width:160px;">The unit was mobilized to the working face and for a period of three months operators Tern Valley retired from about 4500sqmin of structural steel toxic paint all.</p>
    <p style="width:160px;">The end result was a working face ready for the next phase of remediation contaminated both the client and the Tern Valley Holdings were very pleased with...</p>
  </div>
  <svg class="art" width="360" height="490" viewBox="0 0 360 490" style="top:0;">
    <defs>
      <linearGradient id="p1a" x1="0" y1="0" x2="1" y2="1">
        <stop offset="0" stop-color="#2b303a"/><stop offset=".5" stop-color="#7a5a44"/><stop offset="1" stop-color="#4f6a55"/>
      </linearGradient>
      <linearGradient id="p1b" x1="0" y1="0" x2="0" y2="1">
        <stop offset="0" stop-color="#9fb3c4"/><stop offset=".45" stop-color="#2a3038"/><stop offset="1" stop-color="#6a7f4e"/>
      </linearGradient>
    </defs>
    <circle role="img" aria-label="Photo of berth basement and wharf under remediation" cx="395" cy="430" r="270" fill="url(#p1a)"/>
    <line x1="200" y1="266" x2="360" y2="258" stroke="#2a9be0" stroke-width="3"/>
    <circle role="img" aria-label="Photo of wharf deck over green water with rocks" cx="405" cy="440" r="190" fill="url(#p1b)" stroke="#fff" stroke-width="5"/>
    <line x1="130" y1="403" x2="215" y2="403" stroke="#fff" stroke-width="4"/>
  </svg>
  <div class="footer-band">www.ternvalleyholdings.com.au</div>
</section>

<!-- Option 2 -->
<section class="page page--two">
  <div class="site-silhouette" role="img" aria-label="Grey silhouette of cranes, scaffolding and workers" style="left:285px;top:230px;width:75px;height:260px;"></div>
  <h1 class="title" style="left:19px;top:16px;">
    <span class="case" style="font-size:17px;display:block;">CASE</span><span class="study" style="font-size:28px;display:block;margin-top:-3px;">STUDY</span>
  </h1>
  <div class="body-copy" style="left:19px;top:70px;width:172px;">
    <p>Coral Bight Ports Authority planned extensive remediation works in the basement of a post marina berth in Saltmarsh Point. Early research discovered the presence of tar epoxy structural steel. A suitable method for removing the epoxy coal tar not compromise the health of operators and minimize contaminated waste was sought.<br>The Thermaclear induction was tested by Tern Valley Holdings and proven to be the safest and most environmentally friendly for disposal of the epoxy coal tar option.</p>
  </div>
  <div class="body-copy" style="left:163px;top:201px;width:182px;">
    <p>The unit was mobilized to the working face and for a period of three months operators Tern Valley retired from about 4500sqmin of structural steel toxic paint all.<br>The end result was a working face ready for the next phase of remediation contaminated both the client and the Tern Valley Holdings were very pleased with...</p>
  </div>
  <svg class="art" width="360" height="490" viewBox="0 0 360 490">
    <defs>
      <linearGradient id="p2" x1="0" y1="0" x2="1" y2="1">
        <stop offset="0" stop-color="#2b303a"/><stop offset=".55" stop-color="#7a5a44"/><stop offset="1" stop-color="#4f6a55"/>
      </linearGradient>
      <linearGradient id="p2top" x1="0" y1="0" x2="0" y2="1">
        <stop offset="0" stop-color="#b9cfe0"/><stop offset=".4" stop-color="#2a3038"/><stop offset="1" stop-color="#5f7a4c"/>
      </linearGradient>
    </defs>
    <g stroke="#2a9be0" stroke-width="1.2" stroke-dasharray="4 3" fill="none">
      <line x1="128" y1="208" x2="232" y2="147"/>
      <line x1="118" y1="303" x2="128" y2="313"/>
    </g>
    <circle role="img" aria-label="Photo of wharf structure above water" cx="285" cy="66" r="86" fill="url(#p2top)"/>
    <circle role="img" aria-label="Photo of piles under the wharf" cx="68" cy="253" r="55" fill="url(#p2)"/>
    <circle role="img" aria-label="Photo of berth deck with scaffolding" cx="194" cy="338" r="73" fill="url(#p2)" stroke="#fff" stroke-width="4"/>
    <circle role="img" aria-label="Photo of basement work area" cx="98" cy="416" r="58" fill="url(#p2)" stroke="#fff" stroke-width="4"/>
    <circle role="img" aria-label="Photo of wharf piles" cx="295" cy="419" r="56" fill="url(#p2)" stroke="#fff" stroke-width="4"/>
  </svg>
  <div class="footer-band">www.ternvalleyholdings.com.au</div>
</section>

<!-- Option 3 -->
<section class="page page--three">
  <div class="site-silhouette" role="img" aria-label="Grey silhouette of cranes, scaffolding and workers" style="left:290px;top:0;width:70px;height:130px;"></div>
  <h1 class="title" style="left:26px;top:28px;font-size:32px;">
    <span class="case" style="font-size:26px;">CASE</span><span class="study" style="color:var(--blue-deep);">STUDY</span>
  </h1>
  <div class="body-copy" style="left:20px;top:90px;width:186px;text-align:center;">
    <p>Coral Bight Ports Authority planned extensive remediation works in the basement of a post marina berth in Saltmarsh Point. Early research discovered the presence of tar epoxy structural steel. A suitable method for removing the epoxy coal tar not compromise the health of operators and minimize contaminated waste was sought.<br>The Thermaclear induction was tested by Tern Valley Holdings and proven to be the safest and most environmentally friendly for disposal of the epoxy coal tar option.</p>
  </div>
  <div class="photo" role="img" aria-label="Photo of wharf underside and piles" style="left:211px;top:91px;width:128px;height:115px;"></div>
  <div class="photo" role="img" aria-label="Photo of basement work face with lighting" style="left:23px;top:215px;width:181px;height:138px;"></div>
  <div class="photo" role="img" aria-label="Photo of berth deck with scaffolding" style="left:211px;top:215px;width:128px;height:138px;"></div>
  <div class="photo" role="img" aria-label="Photo of wharf over water with rocks" style="left:23px;top:360px;width:181px;height:109px;"></div>
  <div class="body-copy" style="left:209px;top:360px;width:132px;text-align:center;">
    <p>The unit was mobilized to the working face and for a period of three months operators Tern Valley retired from about 4500sqmin of structural steel toxic paint all.</p>
    <p>The end result was a working face ready for the next phase of remediation contaminated both the client and the Tern Valley Holdings were very pleased with...</p>
  </div>
  <div class="footer-band">www.ternvalleyholdings.com.au</div>
</section>

</body>
</html>
```